Family Values Poster

Need a poster for my kids (ages 5-8) that says:
Be Smart
Be Kind
Be Curious
Be Grateful
We Love You

fun, but hopefully something that they will keep for a long time

Target Market(s)

my kids

Requirements
Must have
• vertical
Nice to have
• fun and attention grabbing
Should not have
• look cheesy - not a generic inspirational poster

```html
<!DOCTYPE html>
<html lang="en">
<head>
<meta charset="utf-8">
<title>Family Values Poster</title>
<link rel="stylesheet" href="https://fonts.googleapis.com/css2?family=Domine:wght@700&display=swap">
<style>
  :root {
    --backdrop: #e6e6e6;
    --ink: #ffffff;
    --deep-blue: #0c14c8;
    --ocean: #1a5fb0;
    --leaf: #3fd83a;
    --lime: #6cc51c;
    --coral: #f0605a;
    --amber: #c8702a;
    --violet: #8a2aa8;
    --frame: #ffffff;
  }
  * { box-sizing: border-box; margin: 0; padding: 0; }
  html, body {
    width: 1040px; height: 1200px; overflow: hidden;
    background: var(--backdrop);
  }
  .poster {
    position: absolute; left: 55px; top: 0;
    width: 930px; height: 1200px; overflow: hidden;
    background:
      radial-gradient(ellipse 260px 320px at 0% 5%, var(--deep-blue) 0%, rgba(12,20,200,0) 100%),
      radial-gradient(ellipse 300px 520px at 5% 35%, var(--ocean) 0%, rgba(26,95,176,0) 100%),
      radial-gradient(ellipse 160px 220px at 100% 0%, var(--coral) 0%, rgba(240,96,90,0) 100%),
      radial-gradient(ellipse 300px 260px at 8% 95%, var(--amber) 0%, rgba(200,112,42,0) 100%),
      radial-gradient(ellipse 260px 220px at 42% 92%, var(--violet) 0%, rgba(138,42,168,0) 100%),
      radial-gradient(ellipse 240px 200px at 55% 100%, #c23a4a 0%, rgba(194,58,74,0) 100%),
      radial-gradient(ellipse 260px 240px at 40% 50%, #1fb0a0 0%, rgba(31,176,160,0) 100%),
      linear-gradient(160deg, #2a9a6a 0%, var(--leaf) 40%, var(--lime) 70%, #4a9a18 100%);
  }
  .value {
    position: absolute;
    font-family: "Domine", Georgia, serif;
    font-weight: 700; font-size: 58px; line-height: 1;
    color: var(--ink);
    white-space: nowrap;
    text-shadow: 0 1px 2px rgba(0,0,0,0.15);
  }
  .rule {
    position: absolute; height: 2px; background: var(--ink);
  }
  .photo {
    position: absolute; width: 384px; height: 214px;
    border: 6px solid var(--frame); border-radius: 4px;
    box-shadow: 0 2px 6px rgba(0,0,0,0.2);
  }
  .photo--garden  { background: linear-gradient(135deg, #4a4a38, #7a6a50 50%, #3a5a70); }
  .photo--reading { background: linear-gradient(135deg, #8a8a50, #d8a050 55%, #5a3a50); }
  .photo--portrait{ background: linear-gradient(135deg, #3a3a3a, #9a9a9a 55%, #505050); }
  .photo--porch   { background: linear-gradient(160deg, #5a7a4a, #8a8a80 50%, #6a6a68); }
  .photo--cuddle  { background: linear-gradient(135deg, #f4ece6, #e8dcd0 50%, #c8d4e0); }
</style>
</head>
<body>
  <main class="poster">
    <div class="photo photo--garden" style="left:489px; top:79px;" role="img" aria-label="Photo of a young girl watering plants in a garden"></div>
    <div class="value" style="left:90px; top:166px;">Be Smart</div>
    <div class="rule" style="left:182px; top:222px; width:307px;"></div>

    <div class="photo photo--reading" style="left:70px; top:280px;" role="img" aria-label="Photo of two girls reading a book together outdoors at sunset"></div>
    <div class="value" style="left:510px; top:367px;">Be Kind</div>
    <div class="rule" style="left:454px; top:428px; width:304px;"></div>

    <div class="photo photo--portrait" style="left:489px; top:482px;" role="img" aria-label="Black and white photo of a boy in a library"></div>
    <div class="value" style="left:94px; top:568px;">Be Curious</div>
    <div class="rule" style="left:182px; top:629px; width:307px;"></div>

    <div class="photo photo--porch" style="left:83px; top:683px;" role="img" aria-label="Photo of a baby and an older sister sitting on a wooden deck"></div>
    <div class="value" style="left:512px; top:768px;">Be Grateful</div>
    <div class="rule" style="left:467px; top:829px; width:308px;"></div>

    <div class="photo photo--cuddle" style="left:489px; top:885px;" role="img" aria-label="Photo of a mother cuddling her child on a white sofa"></div>
    <div class="value" style="left:71px; top:996px;">We Love You</div>
    <div class="rule" style="left:182px; top:1063px; width:307px;"></div>
  </main>
</body>
</html>
```